card for Hollis Handyman & Yard business, double sided with services listed on the back

Design a business card for a Hollis Handyman & Yard business in San Jose,ca. Would like front to be a house with 3D characters doing different tasks i.e. Mowing lawn, painting, sprinklers, lighting, weed whacking, power washing, lumber etc. on the backside a cutout of the interior with computer, internet, cleaning, bathroom/kitchen remodeling, smart home etc.

Industry/Entity Type

Handyman

Contact Information for Business Card

Two sided view of a house, one outside services and one inside services

Colors

Designer to choose colors to be used in the design.

Requirements
Must have
• General Household Repairs and Maintenance
• Landscaping, Gardening, and Planting
• Painting, Patching and Trim/Moulding Work
• Cleaning, Restoring and Hauling/Trash Removal
• Blinds, Curtains, and Assembly Work
• Computer, Internet/Wireless, and Smart Home Service

```html
<!DOCTYPE html>
<html lang="en">
<head>
<meta charset="utf-8">
<title>Hollis Handyman &amp; Yard – Business Card</title>
<link href="https://fonts.googleapis.com/css2?family=Oxygen:wght@400;700&display=swap" rel="stylesheet">
<style>
  :root{
    --backdrop:#45413a;
    --card-white:#ffffff;
    --brand-blue:#2f5a98;
    --brand-orange:#f5b232;
    --text-dark:#2a2a2a;
    --text-white:#ffffff;
  }
  html,body{margin:0;padding:0;width:1200px;height:1000px;overflow:hidden;background:var(--backdrop);font-family:'Oxygen',sans-serif;}
  .canvas{position:relative;width:1200px;height:1000px;}
  .card{position:absolute;left:250px;width:700px;height:400px;border-radius:34px;overflow:hidden;background:var(--card-white);box-shadow:0 10px 30px rgba(0,0,0,.35);}
  .card--front{top:60px;}
  .card--back{top:540px;background:var(--brand-orange);}
  .card-shapes{position:absolute;inset:0;width:100%;height:100%;}
  .company-name{position:absolute;margin:0;font-weight:700;color:var(--brand-blue);line-height:1.05;}
  .card--front .company-name{left:42px;top:88px;font-size:34px;}
  .card--back .company-name{left:0;right:0;top:48px;text-align:center;font-size:32px;}
  .service-list{position:absolute;right:40px;top:28px;margin:0;padding:0;list-style:none;text-align:right;font-size:17px;line-height:1.22;color:var(--text-dark);}
  .owner-name{position:absolute;left:48px;top:182px;margin:0;font-size:38px;line-height:1.2;font-weight:700;color:var(--brand-blue);}
  .contact-list{position:absolute;left:44px;top:298px;margin:0;padding:0;list-style:none;font-size:18px;line-height:1.25;color:var(--text-dark);}
  .contact-list li{display:flex;align-items:center;gap:12px;}
  .contact-icon{width:14px;height:14px;flex:none;}
  .interior-services{position:absolute;left:0;right:0;top:210px;margin:0;padding:0;list-style:none;text-align:center;font-size:24px;font-weight:700;line-height:1.25;color:var(--text-white);}
</style>
</head>
<body>
<main class="canvas">

  <section class="card card--front" aria-label="Card front">
    <svg class="card-shapes" viewBox="0 0 700 400" preserveAspectRatio="none" aria-hidden="true">
      <path fill="var(--brand-blue)" d="M0 258 C130 246 300 232 470 224 C330 238 160 262 0 310 Z"/>
      <path fill="var(--brand-orange)" d="M0 292 C150 260 330 240 500 229 C600 222 665 196 700 160 L700 400 L0 400 Z"/>
    </svg>
    <h1 class="company-name">Hollis Handyman<br>&amp; Yard</h1>
    <ul class="service-list">
      <li>Mowing lawn</li><li>Painting</li><li>Sprinklers</li><li>Lighting</li>
      <li>Weed Whacking</li><li>Power Washing</li><li>Lumber</li>
    </ul>
    <p class="owner-name">Marcus Delaney</p>
    <ul class="contact-list">
      <li><svg class="contact-icon" viewBox="0 0 14 14"><path fill="var(--card-white)" d="M3 1 L5 1 L6 4 L4.5 5 C5.5 7.5 6.5 8.5 9 9.5 L10 8 L13 9 L13 11 C13 12 12 13 11 13 C5.5 12.5 1.5 8.5 1 3 C1 2 2 1 3 1Z"/></svg>408-555-0147</li>
      <li><svg class="contact-icon" viewBox="0 0 14 14"><rect x="1" y="3" width="12" height="8" fill="var(--card-white)"/><path d="M1 3 L7 8 L13 3" fill="none" stroke="var(--brand-orange)" stroke-width="1.2"/></svg>marcus@hollishandyman.com</li>
      <li><svg class="contact-icon" viewBox="0 0 14 14"><circle cx="5" cy="9" r="3" fill="none" stroke="var(--card-white)" stroke-width="1.8"/><circle cx="9" cy="5" r="3" fill="none" stroke="var(--card-white)" stroke-width="1.8"/></svg>www.hollishandyman.com</li>
      <li><svg class="contact-icon" viewBox="0 0 14 14"><path fill="var(--card-white)" d="M7 13 C3 8 2.5 6.5 2.5 5 A4.5 4.5 0 0 1 11.5 5 C11.5 6.5 11 8 7 13Z"/><circle cx="7" cy="5" r="1.6" fill="var(--brand-orange)"/></svg>Dummy, st suite, Zipcode 12345</li>
    </ul>
  </section>

  <section class="card card--back" aria-label="Card back">
    <svg class="card-shapes" viewBox="0 0 700 400" preserveAspectRatio="none" aria-hidden="true">
      <path fill="var(--card-white)" d="M0 200 C200 190 420 175 560 140 C620 125 670 100 700 85 L700 400 L0 400 Z"/>
      <path fill="var(--brand-blue)" d="M0 250 C60 215 180 200 330 190 C480 180 600 150 700 105 L700 400 L0 400 Z"/>
    </svg>
    <h2 class="company-name">Hollis Handyman &amp; Yard</h2>
    <ul class="interior-services">
      <li>A Cutout Of The Interior With Computer</li>
      <li>Internet, Cleaning</li>
      <li>Bathroom/kitchen Remodeling</li>
      <li>Smart Home Etc</li>
    </ul>
  </section>

</main>
</body>
</html>
```